Direct mail campaign for roofing company

We are a roofing company looking to catch the eye of homeowners using direct mail post cards the are 6x9. We want to advertise that we are who to call for all your roofing needs. This need to be front and back
Crest Roofing
888.517.CRST
crestroofingpro.example

Target Market(s)

Single family homes

Industry/Entity Type

Roofing

Colors

Designer to choose colors to be used in the design.

```html
<!DOCTYPE html>
<html lang="en">
<head>
<meta charset="utf-8">
<title>Crest Roofing – Direct Mail Postcard</title>
<link rel="stylesheet" href="https://fonts.googleapis.com/css2?family=Montserrat:wght@500;700;800;900&family=Open+Sans:wght@400;600;700&display=swap">
<style>
  :root{
    --bg:#8a8a8a;
    --paper:#ffffff;
    --gold:#f2b01e;
    --gold-deep:#d99a12;
    --ink:#161616;
    --slate:#4a4a4c;
    --slate-light:#6b6b6e;
    --muted:#555555;
  }
  *{box-sizing:border-box;margin:0;padding:0}
  html,body{width:900px;height:1200px;overflow:hidden}
  body{background:var(--bg);position:relative;font-family:"Open Sans",sans-serif;color:var(--ink)}

  .postcard{position:absolute;left:40px;width:820px;height:547px;background:var(--paper);overflow:hidden;box-shadow:0 6px 18px rgba(0,0,0,.25)}
  .postcard--front{top:40px}
  .postcard--back{top:613px}
  .postcard__art{position:absolute;inset:0;width:100%;height:100%}

  /* FRONT */
  .brand{position:absolute;left:30px;top:28px;display:flex;align-items:center;gap:10px}
  .brand__mark{width:22px;height:22px;background:var(--ink)}
  .brand__name{font-family:"Montserrat",sans-serif;font-weight:800;font-size:17px;letter-spacing:.5px;color:var(--ink)}
  .front__lead{position:absolute;left:30px;top:118px;width:280px;font-size:11px;font-weight:600;color:var(--muted)}
  .front__banner{position:absolute;left:0;top:140px;width:320px;height:98px;background:var(--gold);padding:10px 0 0 30px}
  .front__headline{font-family:"Montserrat",sans-serif;font-weight:900;font-size:36px;line-height:1.08;color:var(--ink);text-transform:uppercase}
  .front__url{position:absolute;left:30px;top:256px;font-family:"Montserrat",sans-serif;font-weight:800;font-size:15px;color:var(--gold);text-transform:uppercase}

  /* BACK */
  .stamp{position:absolute;right:38px;top:28px;width:62px;height:74px;border:1.5px solid #9a9a9a}
  .address-lines{position:absolute;right:38px;top:170px;width:250px}
  .address-lines span{display:block;height:1px;background:#c4c4c4;margin-bottom:26px}
  .back__panel{position:absolute;left:26px;top:24px;width:300px;color:var(--ink)}
  .section-title{font-family:"Montserrat",sans-serif;font-weight:800;font-size:12px;letter-spacing:.6px;color:var(--paper);text-transform:uppercase;margin-bottom:5px}
  .mission__text{font-size:8.6px;line-height:1.45;width:255px;margin-bottom:16px}
  .services{display:grid;grid-template-columns:1fr 1fr;gap:10px 10px;width:285px;margin-bottom:18px}
  .service{display:flex;align-items:center;gap:6px;font-family:"Montserrat",sans-serif;font-weight:700;font-size:8.4px;line-height:1.25;color:var(--paper)}
  .service__icon{flex:none;width:22px;height:22px}
  .reach{font-size:9px;line-height:1.55}
  .reach__row{display:flex;align-items:center;gap:6px;font-weight:600}
  .reach__row svg{width:10px;height:10px;flex:none}
  .reach__name{font-weight:700}
</style>
</head>
<body>

<section class="postcard postcard--front" aria-label="Postcard front">
  <svg class="postcard__art" viewBox="0 0 820 547" aria-hidden="true">
    <defs>
      <linearGradient id="roofPhoto" x1="0" y1="0" x2="1" y2="1">
        <stop offset="0" stop-color="#7d8a6a"/>
        <stop offset=".45" stop-color="#9c4b32"/>
        <stop offset="1" stop-color="#5e4a3e"/>
      </linearGradient>
    </defs>
    <polygon points="0,547 0,430 820,60 820,150 170,547" fill="var(--ink)"/>
    <polygon points="170,547 820,150 820,547" fill="var(--slate)"/>
    <polygon points="360,300 480,80 760,80 820,190 820,470 720,520 480,520" fill="var(--gold)"/>
    <polygon points="330,260 440,60 610,60 720,260 610,460 440,460" fill="none" stroke="#ffffff" stroke-width="2" opacity=".8"/>
    <polygon points="230,420 290,320 410,320 470,420 410,520 290,520" fill="none" stroke="#ffffff" stroke-width="1.5" opacity=".7"/>
  </svg>
  <svg class="postcard__art" viewBox="0 0 820 547" role="img" aria-label="Aerial photograph of a house with a red tiled roof in a suburban neighborhood">
    <polygon points="360,245 470,45 700,45 810,245 700,445 470,445" fill="url(#roofPhoto)"/>
  </svg>

  <div class="brand"><span class="brand__mark"></span><span class="brand__name">CREST ROOFING</span></div>
  <p class="front__lead">Your roof deserves the team the neighbors trust.</p>
  <div class="front__banner"><h1 class="front__headline">Protect<br>your home!</h1></div>
  <p class="front__url">crestroofingpro.example</p>
</section>

<section class="postcard postcard--back" aria-label="Postcard back">
  <svg class="postcard__art" viewBox="0 0 820 547" aria-hidden="true">
    <defs>
      <linearGradient id="crewPhotoA" x1="0" y1="0" x2="1" y2="1">
        <stop offset="0" stop-color="#8fb3cf"/><stop offset="1" stop-color="#6a5a48"/>
      </linearGradient>
      <linearGradient id="crewPhotoB" x1="0" y1="0" x2="1" y2="1">
        <stop offset="0" stop-color="#a3a9ad"/><stop offset="1" stop-color="#4f5357"/>
      </linearGradient>
      <linearGradient id="crewPhotoC" x1="0" y1="0" x2="1" y2="1">
        <stop offset="0" stop-color="#c7a24a"/><stop offset="1" stop-color="#5d6b7a"/>
      </linearGradient>
    </defs>
    <polygon points="0,547 0,470 820,300 820,380 360,547" fill="var(--ink)"/>
    <polygon points="360,547 820,380 820,547" fill="var(--slate)"/>
    <polygon points="14,14 340,14 340,230 560,230 600,300 520,440 340,470 14,520" fill="var(--gold)"/>
    <polygon points="300,300 350,215 450,215 500,300 450,385 350,385" fill="none" stroke="#ffffff" stroke-width="1.5" opacity=".8"/>
  </svg>
  <svg class="postcard__art" viewBox="0 0 820 547" role="img" aria-label="Photographs of roofers working on a shingle roof and installing roofing material">
    <polygon points="455,255 490,195 560,195 595,255 560,315 490,315" fill="url(#crewPhotoA)"/>
    <polygon points="360,360 400,290 480,290 520,360 480,430 400,430" fill="url(#crewPhotoB)"/>
    <polygon points="510,385 545,325 615,325 650,385 615,445 545,445" fill="url(#crewPhotoC)"/>
  </svg>

  <div class="stamp"></div>
  <div class="address-lines"><span></span><span></span><span></span></div>

  <div class="back__panel">
    <h2 class="section-title">Our Mission</h2>
    <p class="mission__text">At Crest Roofing we protect the homes and families of our community with honest pricing, quality materials and skilled crews. From minor repairs to full replacements, we treat every roof like our own.</p>

    <h2 class="section-title">Services</h2>
    <ul class="services" style="list-style:none">
      <li class="service">
        <svg class="service__icon" viewBox="0 0 22 22" aria-hidden="true"><rect width="22" height="22" fill="#ffffff"/><path d="M4 12 L11 5 L18 12 M6 11 V17 H16 V11" fill="none" stroke="#161616" stroke-width="1.6"/></svg>
        <span>New/Commercial<br>Roof Replacement</span>
      </li>
      <li class="service">
        <svg class="service__icon" viewBox="0 0 22 22" aria-hidden="true"><rect width="22" height="22" fill="#ffffff"/><path d="M5 17 H17 M7 17 V9 H15 V17 M7 9 L11 5 L15 9" fill="none" stroke="#161616" stroke-width="1.6"/></svg>
        <span>New<br>Construction</span>
      </li>
      <li class="service">
        <svg class="service__icon" viewBox="0 0 22 22" aria-hidden="true"><rect width="22" height="22" fill="#ffffff"/><path d="M12 4 L7 12 H11 L9 18 L15 9 H11 Z" fill="#161616"/></svg>
        <span>Storm Damage<br>Roof Replacement</span>
      </li>
      <li class="service">
        <svg class="service__icon" viewBox="0 0 22 22" aria-hidden="true"><rect width="22" height="22" fill="#ffffff"/><path d="M6 16 L13 9 M12 6 L16 10 L14 12 L10 8 Z" fill="none" stroke="#161616" stroke-width="1.8"/></svg>
        <span>Repairs &amp;<br>Restoration</span>
      </li>
    </ul>

    <h2 class="section-title">Reach Us</h2>
    <div class="reach">
      <p class="reach__name">Crest Roofing</p>
      <p class="reach__row"><svg viewBox="0 0 10 10" aria-hidden="true"><path d="M2 1 L4 1 L4.8 3 L3.6 4 Q4.6 6 6 6.4 L7 5.2 L9 6 L9 8 Q5 9 1 3 Z" fill="#161616"/></svg>888.517.CRST</p>
      <p class="reach__row"><svg viewBox="0 0 10 10" aria-hidden="true"><circle cx="5" cy="5" r="4" fill="none" stroke="#161616" stroke-width="1.2"/><path d="M1 5 H9 M5 1 Q2.5 5 5 9 Q7.5 5 5 1" fill="none" stroke="#161616" stroke-width=".9"/></svg>crestroofingpro.example</p>
    </div>
  </div>
</section>

</body>
</html>
```